New College Graduate Resume - Creative and unique design that stands out from the rest

Need creative resume design for recent college graduate who graduated from School of Music with a concentration in music composition and production. Striving for a contemporary layout/design that allows the resume to "be unique" and "stand out" but be polished and professional. Open to integrating moderate color/graphics as part of resume design but the design can be minus those attributes as well. Attached is raw content in 7 sections (name/contact info, education, highlights of qualifications, work experience, honors/awards, and professional affiliations). While the designer has full latitude over overall design which (section headers, font type, separation/spacing, use of bullets, justification of text, etc.) please maintain current order/sequence of the 7 sections.

Industry/Entity Type

School

Requirements
Must have
• Name (Tobias Garrick Elwin III) should be most prominent (bold/font size) compared to remainder of resume copy.
• Section headers should be prominent but less so when compared to name on resume.
• The attached file of resume content is provided as raw source copy and is NOT to be just copied and pasted into open fields as is. Expectation is each section of copy will be organized in a manner that is most visually appealing and may include bullets, appropriate spacing, etc.
Should not have
• The attached file of resume content is provided as source copy and is NOT to be just copied and pasted into open fields as is. Expectation is each section of copy will be organized in a manner that

```html
<!DOCTYPE html>
<html lang="en">
<head>
<meta charset="utf-8">
<title>Tobias Garrick Elwin III — Resume</title>
<link rel="stylesheet" href="https://fonts.googleapis.com/css2?family=Roboto+Condensed:wght@400;700&display=swap">
<style>
  :root {
    --backdrop: #dccdb2;
    --charcoal: #333335;
    --orange: #ef8f1d;
    --orange-deep: #e07f12;
    --teal: #139a94;
    --white: #ffffff;
  }
  * { box-sizing: border-box; margin: 0; padding: 0; }
  html, body { width: 1200px; height: 898px; overflow: hidden; }
  body {
    background: var(--backdrop);
    font-family: "Roboto Condensed", "Arial Narrow", sans-serif;
    color: var(--white);
  }
  .resume {
    position: absolute;
    left: 290px; top: 10px;
    width: 620px; height: 878px;
    background: var(--charcoal);
    overflow: hidden;
    box-shadow: 0 6px 18px rgba(0,0,0,.25);
  }
  /* Sidebar */
  .sidebar {
    position: absolute; left: 0; top: 0;
    width: 248px; height: 100%;
    background: var(--orange);
  }
  .name-band {
    position: absolute; left: 0; top: 52px;
    width: 262px; height: 150px;
    background: var(--teal);
    clip-path: polygon(0 0, 100% 0, 100% 88%, 94% 100%, 0 100%);
    padding: 14px 0 0 22px;
  }
  .name {
    font-weight: 700; font-size: 46px; line-height: 40px;
    text-transform: uppercase; letter-spacing: -1.5px;
  }
  .contact { position: absolute; left: 22px; top: 230px; width: 220px; }
  .contact-item { display: flex; gap: 8px; align-items: flex-start; margin-bottom: 22px; font-size: 16px; line-height: 19px; }
  .contact-item svg { flex: none; margin-top: 2px; }
  .contact-item small { font-size: 9px; }
  .highlights-band {
    position: absolute; left: 0; top: 420px;
    width: 262px; height: 66px;
    background: var(--teal);
    clip-path: polygon(0 0, 100% 0, 100% 86%, 94% 100%, 0 100%);
    padding: 10px 0 0 26px;
    font-size: 22px; line-height: 22px; font-weight: 700; text-transform: uppercase; letter-spacing: -.5px;
  }
  .skills { position: absolute; left: 34px; top: 502px; width: 208px; list-style: none; }
  .skills li {
    font-size: 13.5px; line-height: 16px; font-weight: 700; text-transform: uppercase;
    margin-bottom: 8px; padding-left: 9px; text-indent: -9px;
  }
  .skills li::before { content: "• "; }
  /* Main column */
  .main { position: absolute; left: 262px; top: 0; width: 358px; padding: 22px 20px 0 16px; }
  .section { margin-bottom: 13px; }
  .tag {
    display: inline-block;
    background: var(--orange);
    font-weight: 700; font-size: 14px; line-height: 20px; text-transform: uppercase;
    padding: 0 18px 0 10px;
    clip-path: polygon(0 0, 100% 0, calc(100% - 10px) 100%, 0 100%);
    margin-bottom: 4px;
  }
  .tag.teal { background: var(--teal); }
  .tag-inline { display: flex; align-items: flex-end; gap: 4px; }
  .tag-inline .tag { margin-bottom: 0; flex: none; }
  .body { font-size: 9.6px; line-height: 12.4px; }
  .justify { text-align: justify; }
  .accent { color: var(--orange); }
  .entry { margin-bottom: 7px; }
  .divider { border-left: 2px solid var(--orange-deep); padding-left: 8px; }
</style>
</head>
<body>
<article class="resume">
  <aside class="sidebar">
    <div class="name-band">
      <h1 class="name">Tobias<br>Garrick<br>Elwin III</h1>
    </div>
    <address class="contact" style="font-style:normal">
      <div class="contact-item">
        <svg width="14" height="18" viewBox="0 0 14 18" aria-hidden="true"><path d="M7 1C3.7 1 1 3.6 1 6.9 1 11 7 17 7 17s6-6 6-10.1C13 3.6 10.3 1 7 1z" fill="none" stroke="#fff" stroke-width="1.6"/><circle cx="7" cy="7" r="2" fill="#fff"/></svg>
        <span>217 Larkspur Lane<br>Atlanta, Georgia 30318</span>
      </div>
      <div class="contact-item">
        <svg width="16" height="16" viewBox="0 0 16 16" aria-hidden="true"><circle cx="8" cy="8" r="7" fill="none" stroke="#fff" stroke-width="1.3"/><path d="M5.5 4.5l1.4 1.6-.8 1c.5 1 1.3 1.8 2.3 2.3l1-.8 1.6 1.4-.9 1.2C7.7 11 5 8.3 4.3 5.4z" fill="#fff"/></svg>
        <span>404-555-0186 <small>(cell)</small></span>
      </div>
      <div class="contact-item">
        <svg width="16" height="12" viewBox="0 0 16 12" aria-hidden="true"><rect x="1" y="1" width="14" height="10" fill="none" stroke="#fff" stroke-width="1.3"/><path d="M1 1l7 6 7-6" fill="none" stroke="#fff" stroke-width="1.3"/></svg>
        <span>tgelwin212@mailbox.com</span>
      </div>
    </address>
    <h2 class="highlights-band">Highlights of<br>Qualifications</h2>
    <ul class="skills">
      <li>Media production software (SoundDesk 11)</li>
      <li>Sound design</li>
      <li>Sound acoustics</li>
      <li>Studio recording</li>
      <li>Audio editing</li>
      <li>Audio mixing</li>
      <li>Analog/digital board operation</li>
      <li>Music arranging</li>
      <li>Music composition</li>
      <li>Music production</li>
      <li>Composing sheet music</li>
      <li>Singer-songwriter</li>
      <li>Rhythm guitarist</li>
    </ul>
  </aside>

  <main class="main">
    <section class="section">
      <h2 class="tag">Profile</h2>
      <p class="body justify">Recent graduate of a highly ranked university seeking opportunities to apply composition and production talents across a variety of music genres and other media. Expertise lies in delivering high quality sound design, editing, mixing, and recording. Excellent interpersonal skills and the ability to build strong relationships with people at all levels. Exceptionally motivated self-starter and creative problem solver who enjoys working collaboratively on teams.</p>
    </section>

    <section class="section">
      <h2 class="tag teal">Education</h2>
      <div class="body">
        <div class="entry"><span class="accent">Bayview University</span> – Halloran School of Music<br>Coral Springs, Florida</div>
        <div class="entry"><span class="accent">Bachelor of Music – May 2016</span><br>Major: Media Writing and Production, GPA 3.20/4.0</div>
        <div class="entry"><span class="accent">Ridgemont Academy</span><br>College Park, Georgia<br>High School Diploma with Honors – <span class="accent">May 2011</span></div>
      </div>
    </section>

    <section class="section">
      <div class="tag-inline"><h2 class="tag">Work Experience</h2><span class="body">- Miami, FL - <span class="accent">May 2014 – Present</span></span></div>
      <div class="body divider">
        <div class="entry justify"><span class="accent">Coastline Film House (CFH)</span><br>Sound Engineer<br>Edited and mixed recorded field audio to professional standards. Matched audio with motion picture video to create a seamless product. Recorded automated dialogue replacement (ADR) audio and integrated into motion picture video project using SoundDesk 11. Recorded foley sound effects to be added to film, video, and other media in post-production. Composed and recorded original music to accompany various video projects.</div>
        <div class="entry justify"><span class="accent">Northpoint Retail</span> - Atlanta, GA - <span class="accent">May 2013 - October 2013</span><br>Sales Associate<br>Provided customer service, maintained a clean and organized work environment, assisted in sales, and performed cashier responsibilities.</div>
        <div class="entry justify"><span class="accent">Peach State Civic Action Group</span><br>Atlanta, GA - <span class="accent">June 2012 - August 2012</span><br>On-Site Promoter/Intern<br>Promoted and advertised various campaigns and managed various office tasks, such as setting up site maps and organizing and sorting non-profit donations.</div>
        <div class="entry justify"><span class="accent">Keystone Marketing, Incorporated</span> - Atlanta, GA - <span class="accent">June 2011 – August 2011</span><br>Product Marketing Consultant<br>Conducted direct sales and marketing of subsidiary product line through establishing a compelling value proposition, overcoming objections, and closing the sale.</div>
      </div>
    </section>

    <section class="section">
      <h2 class="tag">Honors/Awards</h2>
      <div class="body">
        <span class="accent">Best Film and Score:</span> Frights and Scores 2015 Competition (Bayview University)<br>
        Lillian Brooks Scholar<br>
        Best New Member, Delta Rho Kappa Fraternity, Inc.<br>
        Bayview University Homecoming King, 2012
      </div>
    </section>

    <section class="section">
      <h2 class="tag">Professional Affiliations</h2>
      <div class="body">
        <span class="accent">Member,</span> Guild of Concert Composers <span class="accent">(GCC)</span><br>
        <span class="accent">Member,</span> National Alliance of Composers, Authors and Publishers <span class="accent">(NACAP)</span><br>
        <span class="accent">Member,</span> Sound Engineering Association <span class="accent">(SEA)</span><br>
        <span class="accent">Member,</span> Delta Rho Kappa Fraternity, Incorporated
      </div>
    </section>
  </main>
</article>
</body>
</html>
```